clean web design for a recruitment company

We need a web design for a company called 'TORAVI' recruitment. We are a new age recruitment companies that selects people by their true nature, values and what they can bring to the table as a tangible talent. We are all here possessing a certain talent, whatever that could be that the world needs. The final design should communicate professionalism and strongly embedded etiquette we believe in and a branding promise 'Seeing ones true nature'. Our companies values are integrity, giving away to the community, cherishing the sharing of our talent, time and helping one another.

Target Market(s)

Gulf Countries

Industry/Entity Type

It Company

Number of Pages Required

1 page

Font styles to use
Serif

Requirements
Must have
• Clear and readable font, user friendly structure and easy navigation menus.
Nice to have
• Extra sort of ideas on images we may use, tag lines etc. sample sites we love site:https://www.velmaroque.com/
• http://www.dorisaklund.com/
• http://www.pebblemoorhouse.com/idea-gallery/
Should not have
• all sort of colors, big combination of fonts, images with people in the office or people in suits likewise all the typical industry web sites

```html
<!DOCTYPE html>
<html lang="en">
<head>
<meta charset="utf-8">
<title>Toravi Recruitment</title>
<link rel="stylesheet" href="https://fonts.googleapis.com/css2?family=Open+Sans:wght@400;600;700&family=Arimo:wght@400&display=swap">
<style>
:root{
  --ink:#111;
  --text:#555;
  --muted:#777;
  --line:#e3e3e3;
  --grey-btn:#555;
  --nav-top:#2b2b2b;
  --nav-bottom:#000;
  --footer:#2a2a2a;
  --footer-base:#232323;
  --footer-text:#e6e6e6;
  --white:#fff;
}
*{margin:0;padding:0;box-sizing:border-box}
html,body{width:965px;height:1200px;overflow:hidden;background:var(--white)}
body{position:relative;font-family:"Arimo",Arial,sans-serif;color:var(--text)}
.abs{position:absolute}
.top-rule{left:0;top:0;width:965px;height:2px;background:#777}

.brand{left:80px;top:16px;width:70px;text-align:center}
.brand-mark{display:block;width:22px;height:26px;margin:0 auto 6px;border:2px solid var(--ink)}
.brand-name{font-family:"Open Sans",sans-serif;font-weight:600;font-size:17px;color:var(--ink);letter-spacing:.3px}

.search{left:673px;top:43px;width:213px;height:22px;border:1px solid #d4d4d4;border-radius:2px;background:linear-gradient(#fff,#f3f3f3)}
.search-label{position:absolute;left:6px;top:5px;font-size:9px;color:#555}
.search-btn{position:absolute;right:-1px;top:-1px;width:24px;height:22px;background:#111;border-radius:0 2px 2px 0}

.nav{left:79px;top:104px;width:805px;height:36px;background:linear-gradient(var(--nav-top),var(--nav-bottom));border-radius:3px 3px 0 0;list-style:none;font-family:"Open Sans",sans-serif;font-size:10px;color:var(--white)}
.nav li{position:absolute;top:11px;transform:translateX(-50%);white-space:nowrap}

.hero{left:79px;top:140px;width:805px;height:362px}
.hero-title{left:79px;top:290px;width:805px;text-align:center;font-family:"Open Sans",sans-serif;font-weight:600;font-size:29px;color:var(--white);letter-spacing:.3px;text-shadow:0 0 2px #222,1px 1px 2px #222,-1px -1px 1px #222}

.welcome-title{left:0;top:526px;width:965px;text-align:center;font-family:"Open Sans",sans-serif;font-weight:700;font-size:18px;color:var(--ink)}
.welcome-text{left:88px;top:564px;width:789px;text-align:center;font-family:"Open Sans",sans-serif;font-size:8.6px;line-height:18.6px;color:var(--muted)}

.feature{width:170px;text-align:center;transform:translateX(-50%)}
.feature-icon{display:block;margin:0 auto;width:52px;height:52px;border-radius:50%;background:var(--grey-btn)}
.feature-icon.is-active{background:var(--ink)}
.feature-title{margin-top:14px;font-family:"Open Sans",sans-serif;font-size:11px;color:#444}
.feature-text{margin-top:4px;font-size:8px;line-height:17.4px;color:var(--muted)}

.divider{left:79px;top:818px;width:806px;height:1px;background:var(--line)}
.divider-knot{left:478px;top:814px;width:8px;height:8px;border:1px solid #aaa;border-radius:50%;background:var(--white)}

.section-title{font-family:"Open Sans",sans-serif;font-weight:600;font-size:13.5px;color:var(--ink)}
.about-photo{left:79px;top:872px;width:159px;height:118px;border:1px solid #ccc;background:linear-gradient(160deg,#8a8690,#5e5b63 55%,#a5a1a6);box-shadow:0 6px 6px -4px rgba(0,0,0,.35)}
.about-text{left:250px;top:874px;width:350px;font-family:"Open Sans",sans-serif;font-size:8.8px;line-height:16.6px;color:#444}
.read-more{left:250px;top:964px;width:69px;height:26px;border-radius:3px;background:var(--grey-btn);color:var(--white);font-family:"Open Sans",sans-serif;font-size:9.5px;text-align:center;line-height:26px}

.post{left:621px;width:270px}
.post-thumb{position:absolute;left:0;top:0;width:69px;height:49px;border:1px solid #ccc}
.post-body{position:absolute;left:80px;top:1px}
.post-title{font-family:"Open Sans",sans-serif;font-size:10px;color:#222}
.post-text{margin-top:3px;font-family:"Open Sans",sans-serif;font-size:7.8px;line-height:15.6px;color:#444}

.footer{left:0;top:1021px;width:965px;height:143px;background:var(--footer)}
.footer-base{left:0;top:1164px;width:965px;height:36px;background:var(--footer-base);border-top:1px solid #3a3a3a;text-align:center;font-size:8px;color:var(--footer-text);line-height:36px}
.footer-links{list-style:none;top:1036px;font-size:8.8px;line-height:20.8px;color:var(--footer-text)}
.footer-heading{font-family:"Open Sans",sans-serif;font-size:11px;color:var(--footer-text);top:1033px}
.field{left:507px;width:145px;height:23px;background:var(--white);font-size:8px;color:#333;padding:7px 4px}
.sign-up{left:507px;top:1126px;width:64px;height:23px;background:#3d3d3d;color:var(--footer-text);font-family:"Open Sans",sans-serif;font-size:10.5px;text-align:center;line-height:23px}
.contact-text{left:727px;top:1053px;width:157px;font-size:7.8px;line-height:13.6px;color:#bbb;text-align:justify}
.social{top:1106px;width:18px;height:18px;border-radius:2px;background:#6a6a6a}
</style>
</head>
<body>
<div class="abs top-rule"></div>

<div class="abs brand"><span class="brand-mark"></span><span class="brand-name">toravi</span></div>

<div class="abs search"><span class="search-label">Search</span>
  <span class="search-btn"><svg width="24" height="22" viewBox="0 0 24 22"><circle cx="10.5" cy="9.5" r="3.3" fill="none" stroke="#fff" stroke-width="1.4"/><line x1="13" y1="12" x2="16" y2="15" stroke="#fff" stroke-width="1.8"/></svg></span>
</div>

<ul class="abs nav">
  <li style="left:35px">HOME</li>
  <li style="left:126px">TEAM</li>
  <li style="left:239px">METHODOLOGY</li>
  <li style="left:380px">SPECIALIST AREAS</li>
  <li style="left:503px">CLIENTS</li>
  <li style="left:615px">CANDIDATES</li>
  <li style="left:745px">TORAVI GROUP</li>
</ul>

<svg class="abs hero" viewBox="0 0 805 362" role="img" aria-label="Gallery wall of framed black and white portraits">
  <defs>
    <linearGradient id="heroTone" x1="0" y1="0" x2="0" y2="1">
      <stop offset="0" stop-color="#2a2a2a"/>
      <stop offset=".45" stop-color="#6b6864"/>
      <stop offset=".8" stop-color="#4a4845"/>
      <stop offset="1" stop-color="#232323"/>
    </linearGradient>
    <radialGradient id="heroLight" cx=".5" cy=".45" r=".6">
      <stop offset="0" stop-color="#fff" stop-opacity=".18"/>
      <stop offset="1" stop-color="#000" stop-opacity=".25"/>
    </radialGradient>
  </defs>
  <path d="M0 2 H805 V326 Q402 365 0 326 Z" fill="url(#heroTone)"/>
  <path d="M0 2 H805 V326 Q402 365 0 326 Z" fill="url(#heroLight)"/>
  <path d="M0 326 Q402 365 805 326 V332 Q402 372 0 332 Z" fill="#8a8a8a"/>
  <g fill="#c8c8c8" stroke="#333" stroke-width="1.2">
    <circle cx="375" cy="338" r="5"/><circle cx="393" cy="338" r="5" fill="none" stroke="#fff"/><circle cx="411" cy="338" r="5" fill="none" stroke="#fff"/><circle cx="428" cy="338" r="5" fill="none" stroke="#fff"/>
  </g>
</svg>
<div class="abs hero-title">SEEING ONES TRUE NATURE</div>

<h1 class="abs welcome-title">WELCOME</h1>
<p class="abs welcome-text">At vero eos et accusamus et iusto odio dignissimos ducimus qui blanditiis praesentium voluptatum deleniti atque corrupti quos dolores et quas molestias excepturi sint occaecati cupiditate non provident, similique sunt in culpa qui officia deserunt mollitia animi, id est laborum et dolorum fuga. Et harum quidem rerum facilis est praesentium voluptatum<br>deleniti atque corrupti quos dolores et quas molestias</p>

<div class="abs feature" style="left:197px;top:647px">
  <span class="feature-icon is-active"><svg width="52" height="52" viewBox="0 0 52 52"><g fill="#fff"><rect x="18" y="19" width="16" height="2.4"/><rect x="18" y="23.5" width="16" height="2.4"/><rect x="18" y="28" width="16" height="2.4"/><rect x="18" y="32.5" width="16" height="2.4"/></g></svg></span>
  <div class="feature-title">Nam libero tempore</div>
  <p class="feature-text">At vero eos et accusamus et iusto odio<br>blanditiis praesentium voluptatum<br>et quas molestias..</p>
</div>
<div class="abs feature" style="left:390px;top:647px">
  <span class="feature-icon"><svg width="52" height="52" viewBox="0 0 52 52"><rect x="17" y="20" width="14" height="14" rx="2" fill="none" stroke="#fff" stroke-width="1.8"/><path d="M23 29 L24 26 L33 17 L35 19 L26 28 Z" fill="#fff"/></svg></span>
  <div class="feature-title">Nam libero tempore</div>
  <p class="feature-text">At vero eos et accusamus et iusto odio<br>blanditiis praesentium voluptatum<br>et quas molestias..</p>
</div>
<div class="abs feature" style="left:576px;top:647px">
  <span class="feature-icon"><svg width="52" height="52" viewBox="0 0 52 52"><path d="M18 26 Q26 16 34 26 Z" fill="#fff"/><path d="M26 26 V32 Q26 34 24 33" fill="none" stroke="#fff" stroke-width="1.6"/></svg></span>
  <div class="feature-title">Nam libero tempore</div>
  <p class="feature-text">At vero eos et accusamus et iusto odio<br>blanditiis praesentium voluptatum<br>et quas molestias..</p>
</div>
<div class="abs feature" style="left:769px;top:647px">
  <span class="feature-icon"><svg width="52" height="52" viewBox="0 0 52 52"><g fill="#fff"><circle cx="26" cy="22" r="3"/><circle cx="20" cy="24" r="2.4"/><circle cx="32" cy="24" r="2.4"/><path d="M21 33 Q21 26 26 26 Q31 26 31 33 Z"/><path d="M15.5 32 Q15.5 27 20 27 Q21 27 21.5 27.5 Q19.5 29 19.5 32 Z"/><path d="M36.5 32 Q36.5 27 32 27 Q31 27 30.5 27.5 Q32.5 29 32.5 32 Z"/></g></svg></span>
  <div class="feature-title">Nam libero tempore</div>
  <p class="feature-text">At vero eos et accusamus et iusto odio<br>blanditiis praesentium voluptatum<br>et quas molestias..</p>
</div>

<div class="abs divider"></div>
<div class="abs divider-knot"></div>

<h2 class="abs section-title" style="left:79px;top:839px">ABOUT US</h2>
<div class="abs about-photo" role="img" aria-label="City square seen through a diamond-pattern fence"></div>
<p class="abs about-text">Sed ut perspiciatis unde omnis iste natus error sit voluptatem accusantium doloremque laudantium, totam rem aperiam, eaque ipsa quae ab illo inventore verita-tis et quasi architecto beatae vitae &nbsp; dolores eos qui ratione voluptatem sequi nesci-unt. Neque porro quisquam est, qui dolorem ipsum quia dolor sit amet voluptatem qui dolorem ipsum quia dolor sit amet</p>
<div class="abs read-more">READ MORE</div>

<h2 class="abs section-title" style="left:620px;top:838px">RECENT POST</h2>
<div class="abs post" style="top:871px">
  <div class="post-thumb" role="img" aria-label="Black and white interior of a grand hall" style="background:linear-gradient(#bdbdbd,#555 60%,#2a2a2a)"></div>
  <div class="post-body"><div class="post-title">Lorem ipsum dolor sit</div><p class="post-text">Sed ut perspiciatis unde omnis iste natus error<br>&nbsp;sit accusantium doloremque laudantium,</p></div>
</div>
<div class="abs post" style="top:941px">
  <div class="post-thumb" role="img" aria-label="Dark moody portrait photograph" style="background:linear-gradient(90deg,#050505,#2b2b2b 55%,#0a0a0a)"></div>
  <div class="post-body"><div class="post-title">Lorem ipsum dolor sit</div><p class="post-text">Sed ut perspiciatis unde omnis iste natus error<br>&nbsp;sit accusantium doloremque laudantium,</p></div>
</div>

<footer>
  <div class="abs footer"></div>
  <ul class="abs footer-links" style="left:81px"><li>Home</li><li>Team</li><li>Methodology</li><li>Specialist Areas</li><li>Clients</li></ul>
  <ul class="abs footer-links" style="left:210px"><li>Candidates</li><li>Toravi group</li><li>Locations</li><li>Privacy Policy</li><li>Terms &amp; Conditions</li></ul>
  <ul class="abs footer-links" style="left:362px"><li>Resources</li><li>Plan Now</li><li>Locations</li><li>Privacy Policy</li><li>Terms &amp; Conditions</li></ul>
  <h3 class="abs footer-heading" style="left:507px">NEWSLETTER SIGN UP</h3>
  <div class="abs field" style="top:1059px">Enter Name</div>
  <div class="abs field" style="top:1092px">Enter Email Address</div>
  <div class="abs sign-up">SIGN UP</div>
  <h3 class="abs footer-heading" style="left:727px">CONTACT US</h3>
  <p class="abs contact-text">At vero eos et accusamus et iusto odio dignissimos ducimus qui blanditiis prae-sentium voluptatum</p>
  <span class="abs social" style="left:729px"></span>
  <span class="abs social" style="left:750px"></span>
  <span class="abs social" style="left:771px"></span>
  <span class="abs social" style="left:792px"></span>
  <div class="abs footer-base">Copyright 2015 Toravi all right reserved</div>
</footer>
</body>
</html>
```